Business card for Autism Consultancy

I need a double-sided business card for Brightpath Learning Consultancy
Please try to use the colours and graphics in line with our website www.brightpathlearn.nz
Front side
Logo and the name of the company – Brightpath Learning Consultancy
We use Child-Centred, Modern and Innovative approaches
Teaching autistic children to bond, laugh and play
www.brightpathlearn.nz
info@brightpathlearn.nz
phone +64 09 37 615 48
Back side
Photo
Mirela Dunstan
Founder
Postgraduate Autism (Children) Specialist (with Merit)
Qualified by the Faculty of Learning Support and Access Studies (FLSA), Harwell Vale University
mirela@brightpathlearn.nz
phone +64 937 615 48
mobile: +64 20 6283 9150
Please do not convert the text fields to outlines, i.e. I need to be able to edit any text after.
The final design should be either in Adobe Illustrator or Adobe Photoshop format.
The Specs for the business card are:
Full Bleed Size
94 x 58 mm
1110 x 685 pixels
Document Trim Size
91 x 55 mm
1075 x 650 pixels

```html
<!DOCTYPE html>
<html lang="en">
<head>
<meta charset="utf-8">
<title>Brightpath Learning Consultancy – Business Card</title>
<link rel="stylesheet" href="https://fonts.googleapis.com/css2?family=Nunito:wght@400;600;700;800&display=swap">
<style>
  :root {
    --navy: #24417c;
    --navy-deep: #1f3a6f;
    --teal: #4fc7c3;
    --ink: #5b6270;
    --paper: #fbfbfb;
    --backdrop: #e6e8ea;
  }
  * { box-sizing: border-box; margin: 0; padding: 0; }
  html, body { width: 1200px; height: 900px; overflow: hidden; }
  body {
    background: var(--backdrop);
    font-family: "Nunito", sans-serif;
    position: relative;
  }
  .card {
    position: absolute;
    left: 270px;
    width: 660px;
    height: 400px;
    background: var(--paper);
    overflow: hidden;
    box-shadow: 0 6px 18px rgba(0,0,0,0.18);
  }
  .card--front { top: 35px; }
  .card--back { top: 465px; }

  /* Front */
  .brand {
    position: absolute; left: 40px; top: 42px;
    display: flex; align-items: center; gap: 14px;
  }
  .brand__mark { width: 44px; height: 44px; border-radius: 50%; background: var(--teal); }
  .brand__name {
    color: var(--navy); font-weight: 800; font-size: 24px; line-height: 1.05;
  }
  .tagline {
    position: absolute; left: 40px; top: 170px;
    color: var(--ink); font-size: 18px; line-height: 1.35;
  }
  .band {
    position: absolute; left: 0; right: 0; bottom: 0; height: 150px;
    background: var(--navy);
  }
  .band__contacts {
    position: absolute; right: 34px; top: 28px;
    list-style: none; text-align: right;
  }
  .band__contacts li {
    display: flex; justify-content: flex-end; align-items: center; gap: 16px;
    color: #fff; font-size: 18px; line-height: 32px;
  }
  .band__contacts svg { width: 18px; height: 18px; fill: var(--teal); }

  /* Back */
  .portrait { position: absolute; left: 0; top: 0; }
  .person { position: absolute; left: 300px; top: 40px; }
  .person__name { color: var(--navy); font-weight: 800; font-size: 36px; line-height: 1.1; }
  .person__role { color: var(--teal); font-weight: 600; font-size: 21px; margin-top: 2px; }
  .person__contacts { list-style: none; margin-top: 24px; margin-left: -6px; }
  .person__contacts li {
    display: flex; align-items: center; gap: 22px;
    color: var(--ink); font-size: 17px; line-height: 33px;
  }
  .person__contacts svg { width: 20px; height: 20px; fill: var(--navy); }
  .credentials {
    position: absolute; left: 30px; top: 282px;
    color: var(--ink); font-size: 16px; line-height: 1.55;
  }
</style>
</head>
<body>

<section class="card card--front" aria-label="Card front">
  <div class="brand">
    <span class="brand__mark"></span>
    <span class="brand__name">Brightpath Learning<br>Consultancy</span>
  </div>
  <p class="tagline">We use Child-Centred, Modern and Innovative approaches<br>Teaching autistic children to bond, laugh and play</p>
  <div class="band">
    <ul class="band__contacts">
      <li>www.brightpathlearn.nz
        <svg viewBox="0 0 20 20"><path d="M3 2 L17 9 L10 10.5 L7 17 Z"/></svg></li>
      <li>info@brightpathlearn.nz
        <svg viewBox="0 0 20 20"><path d="M2 6 L10 2 L18 6 V16 H2 Z M2 7 L10 12 L18 7 V8 L10 13 L2 8 Z" fill-rule="evenodd"/></svg></li>
      <li>+64 09 37 615 48
        <svg viewBox="0 0 20 20"><path d="M4 2 L8 2 L9 6 L7 8 C8 11 9 12 12 13 L14 11 L18 12 L18 16 C18 17 17 18 16 18 C8 17 3 12 2 4 C2 3 3 2 4 2 Z"/></svg></li>
    </ul>
  </div>
</section>

<section class="card card--back" aria-label="Card back">
  <svg class="portrait" width="260" height="270" viewBox="0 0 260 270">
    <defs>
      <linearGradient id="photoTone" x1="0" y1="0" x2="0" y2="1">
        <stop offset="0" stop-color="#b89078"/>
        <stop offset="0.55" stop-color="#d7ad93"/>
        <stop offset="1" stop-color="#6b5446"/>
      </linearGradient>
    </defs>
    <circle cx="110" cy="120" r="112" fill="url(#photoTone)" role="img" aria-label="Portrait photo of Mirela Dunstan"/>
    <path d="M150 -20 A128 128 0 0 1 200 205" fill="none" stroke="var(--navy)" stroke-width="14"/>
    <path d="M8 232 A124 124 0 0 0 215 198" fill="none" stroke="var(--teal)" stroke-width="14"/>
  </svg>

  <div class="person">
    <h1 class="person__name">Mirela Dunstan</h1>
    <p class="person__role">Founder</p>
    <ul class="person__contacts">
      <li><svg viewBox="0 0 20 20"><path d="M2 7 L10 3 L18 7 V16 H2 Z M2 8 L10 12 L18 8 V9 L10 13 L2 9 Z" fill-rule="evenodd"/></svg>mirela@brightpathlearn.nz</li>
      <li><svg viewBox="0 0 20 20"><path d="M4 2 L8 2 L9 6 L7 8 C8 11 9 12 12 13 L14 11 L18 12 L18 16 C18 17 17 18 16 18 C8 17 3 12 2 4 C2 3 3 2 4 2 Z"/></svg>+64 937 615 48</li>
      <li><svg viewBox="0 0 20 20"><path d="M6 1 H14 A1.5 1.5 0 0 1 15.5 2.5 V17.5 A1.5 1.5 0 0 1 14 19 H6 A1.5 1.5 0 0 1 4.5 17.5 V2.5 A1.5 1.5 0 0 1 6 1 Z M6.5 3 V15 H13.5 V3 Z M9 16 H11 V17.5 H9 Z" fill-rule="evenodd"/></svg>+64 20 6283 9150</li>
    </ul>
  </div>

  <p class="credentials">Postgraduate Autism (Children) Specialist (with Merit)<br>Qualified by the Faculty of Learning Support and Access Studies (FLSA),<br>Harwell Vale University</p>
</section>

</body>
</html>
```